Design a New Business Card for Our Company

We are looking for fresh, unique, and a modern business card that reflects our roots as digital marketing agency focused on SEM.

Industry/Entity Type

Marketing

Contact Information for Business Card

looking for very unique out of the box designs. clean and modern that compliments our logo

Requirements
Must have
• colors should match our logo
• Front should have name, address, email, and phone/fax of the person, phone/fax are the same number
• back should have our url

```html
<!DOCTYPE html>
<html lang="en">
<head>
<meta charset="utf-8">
<title>Brightwave Solutions – Business Card</title>
<link href="https://fonts.googleapis.com/css2?family=Questrial&display=swap" rel="stylesheet">
<style>
  :root {
    --page-bg: #e9eaec;
    --brand-blue: #4a86c8;
    --brand-blue-deep: #3c6fa6;
    --brand-blue-light: #6fa2da;
    --text-grey: #6e7175;
    --text-dark: #4d5054;
    --logo-grey: #8e9195;
    --strip-grey: #b9bcbf;
    --card-white: #ffffff;
    --card-shade: #eef0f2;
  }
  * { margin: 0; padding: 0; box-sizing: border-box; }
  html, body {
    width: 1200px; height: 950px; overflow: hidden;
    background: var(--page-bg);
    font-family: "Questrial", "Century Gothic", sans-serif;
  }
  .canvas { position: relative; width: 1200px; height: 950px; }

  .card {
    position: absolute; width: 700px; height: 400px;
    box-shadow: 0 10px 30px rgba(0,0,0,.18);
    overflow: hidden;
  }

  /* Back side */
  .card-back {
    left: 90px; top: 50px;
    background: linear-gradient(135deg, var(--brand-blue-light) 0%, var(--brand-blue) 50%, var(--brand-blue-deep) 100%);
  }
  .card-back .brand {
    position: absolute; left: 50%; top: 150px; transform: translateX(-50%);
    display: flex; align-items: center; gap: 16px; white-space: nowrap;
  }
  .card-back .brand-dot { width: 46px; height: 46px; border-radius: 50%; background: #dfe5ec; }
  .card-back .brand-name { font-size: 44px; color: #e6ebf1; }
  .card-back .url {
    position: absolute; left: 0; right: 0; top: 250px; text-align: center;
    color: #d5e2f1; font-size: 22px; letter-spacing: 4px;
  }

  /* Front side */
  .card-front {
    left: 410px; top: 490px;
    background: linear-gradient(160deg, var(--card-white) 0%, var(--card-white) 55%, var(--card-shade) 100%);
  }
  .card-front .brand {
    position: absolute; right: 40px; top: 70px;
    display: flex; align-items: center; gap: 14px; white-space: nowrap;
  }
  .card-front .brand-dot { width: 40px; height: 40px; border-radius: 50%; background: var(--brand-blue); }
  .card-front .brand-name { font-size: 38px; color: var(--logo-grey); }

  .person { position: absolute; left: 40px; top: 150px; }
  .person-name { font-size: 22px; color: var(--logo-grey); }
  .person-role { font-size: 17px; color: var(--brand-blue); margin-top: 4px; }
  .rule-name {
    position: absolute; left: 120px; right: 40px; top: 204px;
    height: 1px; background: var(--brand-blue);
  }

  .contact-list { position: absolute; left: 40px; top: 222px; list-style: none; }
  .contact-list li {
    display: flex; align-items: center; gap: 12px;
    font-size: 18px; color: var(--text-dark); line-height: 30px;
  }
  .contact-list svg { width: 16px; height: 16px; fill: var(--text-grey); }

  .rule-address {
    position: absolute; left: 360px; right: 40px; top: 300px;
    height: 1px; background: var(--brand-blue);
  }
  .address {
    position: absolute; right: 40px; top: 310px; text-align: right;
    font-size: 18px; color: var(--text-dark); line-height: 26px;
  }

  .base-band { position: absolute; left: 0; bottom: 0; width: 700px; height: 24px; }
</style>
</head>
<body>
<main class="canvas">

  <section class="card card-back" aria-label="Business card back">
    <div class="brand">
      <span class="brand-dot"></span>
      <span class="brand-name">Brightwave Solutions</span>
    </div>
    <p class="url">brightwave.example</p>
  </section>

  <section class="card card-front" aria-label="Business card front">
    <div class="brand">
      <span class="brand-dot"></span>
      <span class="brand-name">Brightwave Solutions</span>
    </div>

    <div class="person">
      <p class="person-name">Mark Ellison</p>
      <p class="person-role">President</p>
    </div>
    <div class="rule-name"></div>

    <ul class="contact-list">
      <li>
        <svg viewBox="0 0 16 16" aria-hidden="true"><path d="M1 5c0-2 2-3 7-3s7 1 7 3v1h-4V5H5v1H1zM3 7h10l1 7H2z"/></svg>
        555 0142 7788
      </li>
      <li>
        <svg viewBox="0 0 16 16" aria-hidden="true"><path d="M4 1h8v4H4zM1 6h14v7h-3v-3H4v3H1zM5 11h6v4H5z"/></svg>
        555 0193 4410
      </li>
      <li>
        <svg viewBox="0 0 16 16" aria-hidden="true"><path d="M1 3h14v10H1zM2 4l6 5 6-5v1L8 10 2 5z" fill-rule="evenodd"/></svg>
        mark@brightwave.example
      </li>
    </ul>

    <div class="rule-address"></div>
    <p class="address">1420 Harbor Lane<br>Fairview, NY 10000</p>

    <svg class="base-band" viewBox="0 0 700 24" preserveAspectRatio="none" aria-hidden="true">
      <polygon points="0,0 380,0 370,24 0,24" fill="var(--strip-grey)"/>
      <polygon points="380,0 700,0 700,24 370,24" fill="var(--brand-blue)"/>
    </svg>
  </section>

</main>
</body>
</html>
```